Corvane Collective Web Presence Design and Relaunch

Take existing web files and "clean up" for a a more presentable web landing pad.
posted presently on a site pad CSS template. at www.corvanecollective.org

The site is clunky and unprofessional looking. Needs to be toned down so the urgency is conveyed, but not via a burning planet image.

Target Market(s)

Non-profit climate adaptation group targeting local government land management agencies, special districts and private landholders of natural resource properties.

Industry/Entity Type

Environment

Coding

Coded - Design and coding required

Number of Pages Required

4 page

Font styles to use
Serif
Sans Serif

Requirements
Must have
• Include current logos, aspects if content on current site www.corvanecollective.org
• A regional Pacific Northwest Focus (US & Canada). Content speaking to urgency but respectful of cultural diversity and norms. Sustainability themes. Emphasis on action and implementation.
Nice to have
• link to like minded projects. Appear to future generations. Diversity in thematic areas ecological resiliency, energy, food security and infrastructure.

```html
<!DOCTYPE html>
<html lang="en">
<head>
<meta charset="utf-8">
<title>Corvane Collective</title>
<link rel="stylesheet" href="https://fonts.googleapis.com/css2?family=Libre+Baskerville:wght@400;700&family=Poppins:ital,wght@0,400;0,500;0,600;0,700;1,800&display=swap">
<style>
:root{
  --blue:#0a8fd0;
  --blue-dark:#0573b3;
  --green:#a3cc3f;
  --ink:#2d2d2d;
  --text:#4b4b4b;
  --card:#ebedf0;
  --footer:#333333;
  --white:#ffffff;
}
*{margin:0;padding:0;box-sizing:border-box}
html,body{width:1200px;height:3995px;overflow:hidden;background:var(--white)}
body{position:relative;font-family:"Poppins",sans-serif;color:var(--text)}
.abs{position:absolute}
.serif{font-family:"Libre Baskerville",serif;text-transform:uppercase;color:var(--ink);font-weight:400}
.squiggle{display:block;width:46px;height:8px}

/* header */
.site-header{position:absolute;left:0;top:0;width:1200px;height:85px;background:var(--white);z-index:5}
.brand-badge{position:absolute;left:46px;top:-32px;width:176px;height:172px;border-radius:50%;background:var(--white);z-index:6;display:flex;align-items:flex-end;justify-content:center;padding-bottom:42px}
.brand-name{font-family:"Poppins",sans-serif;font-weight:600;color:var(--blue);font-size:19px;line-height:22px;text-align:center;text-transform:uppercase;letter-spacing:1px}
.main-nav{position:absolute;left:657px;top:34px;display:flex;gap:32px;font-size:13px;font-weight:500;color:#333}
.main-nav .active{color:var(--green)}
.btn{display:inline-flex;align-items:center;justify-content:center;border-radius:24px;font-size:12px;font-weight:600;text-transform:uppercase}
.btn-green{background:var(--green);color:var(--white)}
.btn-white{background:var(--white);color:#333}
.header-cta{position:absolute;left:987px;top:22px;width:123px;height:40px}

/* hero */
.hero{position:absolute;left:0;top:85px;width:1200px;height:820px;background:linear-gradient(180deg,#3a4150 0%,#6b5a55 28%,#c98a4e 50%,#e6a15a 56%,#5a4636 66%,#231c18 78%,#141210 100%)}
.hero-play{position:absolute;left:546px;top:240px;width:68px;height:68px;border-radius:50%;background:var(--white);display:flex;align-items:center;justify-content:center}
.hero-kicker{position:absolute;left:0;width:1200px;top:323px;text-align:center;color:var(--white);font-size:21px;font-weight:500}
.hero-title{position:absolute;left:0;width:1200px;top:345px;text-align:center;color:var(--white);font-family:"Libre Baskerville",serif;font-size:66px;font-weight:700;text-transform:uppercase}
.hero-wave{position:absolute;left:0;top:400px;width:1200px;height:520px}

/* about */
.about-label{left:87px;top:846px;font-size:12.5px;font-weight:600;color:var(--blue);text-transform:uppercase}
.about-title{left:87px;top:870px;font-size:33px;line-height:32px}
.about-text{left:87px;top:977px;width:420px;font-size:14.5px;line-height:22px;color:#444}
.frame-green{left:595px;top:750px;width:503px;height:222px;background:var(--green)}
.photo{background:#888}
.about-photo{left:621px;top:773px;width:452px;height:414px;background:radial-gradient(ellipse at 50% 55%,#6b5440 0%,#4a3a2c 35%,#2f2924 70%,#1e1c1a 100%)}

/* featured */
.section-title{left:0;width:1200px;text-align:center;font-size:34px}
.section-title .squiggle{margin:8px auto 0}
.projects{left:88px;top:1341px;width:1022px;display:grid;grid-template-columns:1fr 1fr;gap:10px 9px}
.project-card{background:var(--card);height:182px;padding:30px 30px 0 30px;display:flex;gap:28px}
.project-icon{width:64px;height:64px;flex:none;margin-top:2px}
.project-card h3{font-family:"Libre Baskerville",serif;font-weight:400;font-size:17px;text-transform:uppercase;color:#333;margin-top:-2px}
.project-card p{font-size:13.3px;line-height:18.5px;color:#555;margin-top:8px}
.projects-hub{left:574px;top:1501px;width:52px;height:52px;border-radius:50%;background:var(--white);border:8px solid #e2e4e8}

/* impact */
.impact-bg{left:0;top:1803px;width:1200px;height:800px}
.impact-title{left:0;width:1200px;top:1888px;text-align:center;color:var(--white);font-size:34px}
.impact-title .squiggle{margin:6px auto 0}
.stat{top:1962px;width:260px;text-align:center;color:var(--white)}
.stat svg{width:62px;height:62px;display:block;margin:0 auto}
.stat-num{font-family:"Poppins",sans-serif;font-style:italic;font-weight:800;font-size:62px;line-height:80px;letter-spacing:1px}
.stat-label{font-family:"Libre Baskerville",serif;font-size:17px;text-transform:uppercase;margin-top:-2px}
.impact-join{left:448px;top:2188px;width:149px;height:46px}
.impact-contact{left:605px;top:2188px;width:148px;height:46px}

/* recent work */
.work-grid{left:88px;top:2485px;width:1022px;display:grid;grid-template-columns:repeat(4,1fr);gap:12px}
.work-tile{position:relative;height:334px;color:var(--white);text-align:center}
.work-tile h4{position:absolute;left:0;right:0;bottom:40px;font-size:17px;font-weight:700}
.work-tile span{position:absolute;left:0;right:0;bottom:18px;font-size:13px}

/* think green */
.green-frame{left:88px;top:2926px;width:527px;height:282px;background:var(--green)}
.globe-photo{left:127px;top:2970px;width:451px;height:483px;background:radial-gradient(circle at 55% 62%,#7c8f53 0%,#4f6236 28%,#c08f66 45%,#8a5a3a 70%,#3a2a22 100%)}
.green-title{left:685px;top:3030px;font-size:34px;line-height:32px}
.progress{left:685px;width:427px}
.progress .label{font-size:13px;font-weight:600;color:#333;text-transform:uppercase}
.progress .track{position:absolute;left:0;top:25px;width:385px;height:12px;border-radius:6px;background:#ececec}
.progress .fill{height:12px;border-radius:6px;background:repeating-linear-gradient(-60deg,var(--c) 0 6px,rgba(255,255,255,.35) 6px 8px)}
.progress .pct{position:absolute;right:0;top:20px;font-size:17px;color:#333}

/* footer */
.site-footer{left:0;top:3548px;width:1200px;height:447px;background:var(--footer);color:var(--white)}
.footer-brand{left:88px;top:3725px;font-family:"Poppins",sans-serif;font-weight:600;color:var(--green);font-size:30px;line-height:36px;text-transform:uppercase;letter-spacing:2px}
.footer-head{font-family:"Libre Baskerville",serif;color:var(--green);font-size:15px;text-transform:uppercase}
.contact-item{left:388px;font-size:12.5px;line-height:22px;padding-left:22px}
.contact-item svg{position:absolute;left:0;top:3px;width:14px;height:14px}
.quick-links{left:654px;top:3680px;list-style:none;font-size:12.5px;line-height:28.5px}
.news-text{left:853px;top:3680px;width:230px;font-size:12.5px;line-height:18px}
.news-form{left:854px;top:3735px;width:257px;height:40px;border-radius:20px;background:var(--white);overflow:hidden}
.news-form span{position:absolute;left:36px;top:11px;font-size:12px;color:#333}
.news-form .send{position:absolute;right:0;top:0;width:40px;height:40px;background:var(--blue);display:flex;align-items:center;justify-content:center}
.social{left:855px;top:3799px;display:flex;gap:8px}
.social i{width:34px;height:34px;border-radius:50%;display:block}
.to-top{left:1130px;top:3903px;width:44px;height:44px;border-radius:50%;background:var(--green);display:flex;align-items:center;justify-content:center}
.copyright{left:0;width:1200px;top:3948px;text-align:center;font-size:13.5px}
</style>
</head>
<body>

<header class="site-header">
  <nav class="main-nav">
    <span class="active">HOME</span><span>ABOUT US</span><span>CAUSES</span><span>EVENTS</span>
  </nav>
  <a class="btn btn-green header-cta">Contact Us</a>
</header>
<div class="brand-badge"><div class="brand-name">Corvane<br>Collective</div></div>

<section class="hero" role="img" aria-label="Wind turbines silhouetted against an orange sunset sky over a lit shoreline">
  <div class="hero-play"><svg width="18" height="20" viewBox="0 0 18 20"><path d="M2 1 L17 10 L2 19Z" fill="#222"/></svg></div>
  <div class="hero-kicker">WELCOME TO</div>
  <h1 class="hero-title">Corvane Collective</h1>
</section>
<svg class="hero-wave" viewBox="0 0 1200 520" preserveAspectRatio="none">
  <path d="M1200 70 C1120 170 1040 210 880 225 C760 235 650 190 520 200 C300 215 80 310 0 480 L0 520 L1200 520Z" fill="var(--blue)"/>
  <path d="M1200 120 C1120 200 1040 240 880 240 C760 240 650 210 520 215 C300 225 80 320 0 490 L0 520 L1200 520Z" fill="#ffffff"/>
</svg>

<div class="abs about-label">Climate Adaptation</div>
<h2 class="abs serif about-title">Implementing<br>Climate Strategies<svg class="squiggle" viewBox="0 0 46 8"><path d="M1 4 Q6 0 11 4 T21 4 T31 4 T41 4" fill="none" stroke="#ccc" stroke-width="2"/></svg></h2>
<p class="abs about-text">Dedicated to taking action the Corvane Collective was created to help bring adaptation strategies to life. Working with local communities we are committed to implementing strategies that will sustain communities throughout the Pacific Northwest for generations to come.</p>
<div class="abs frame-green"></div>
<div class="abs photo about-photo" role="img" aria-label="Cupped hands holding a mound of dark soil"></div>

<h2 class="abs serif section-title" style="top:1257px">Featured Projects<svg class="squiggle" viewBox="0 0 46 8"><path d="M1 4 Q6 0 11 4 T21 4 T31 4 T41 4" fill="none" stroke="#ccc" stroke-width="2"/></svg></h2>
<div class="abs projects">
  <article class="project-card">
    <svg class="project-icon" viewBox="0 0 64 64" fill="none" stroke="var(--green)" stroke-width="2"><circle cx="32" cy="32" r="12"/><path d="M26 30a7 7 0 0 1 12 0M38 34a7 7 0 0 1-12 0"/><circle cx="14" cy="14" r="5"/><path d="M6 50h52M48 10h10v10"/><path d="M8 52l6-10 6 10z"/></svg>
    <div><h3>Adaptation Plans</h3><p>Communities throughout the region have adopted plans to to address our changing climate. Many more are in the process of developing plans. We are here to help these communities with the hard work implementing those plans.</p></div>
  </article>
  <article class="project-card">
    <svg class="project-icon" viewBox="0 0 64 64" fill="none" stroke="var(--green)" stroke-width="2"><rect x="30" y="6" width="24" height="16"/><path d="M34 12h16M34 17h10M6 58L16 26M16 58L22 26M28 58V26M40 58V30M52 58L46 30M10 26h48"/></svg>
    <div><h3>On the Ground....</h3><p>The Collective is familiar and growing throughout the region. Presently our work has us on the ground in keystone watersheds in the Cascade, Willamette, Columbia and Boise basin watersheds.</p></div>
  </article>
  <article class="project-card">
    <svg class="project-icon" viewBox="0 0 64 64" fill="none" stroke="var(--green)" stroke-width="2"><path d="M32 36V20M32 26c-8 0-12-6-12-12 8 0 12 4 12 12zM32 22c0-8 6-12 14-12 0 8-6 12-14 12z"/><path d="M6 40h10l10 6h12c3 0 3 4 0 4H26M16 54h20l18-12c3-2 0-6-3-4l-9 6"/><rect x="6" y="38" width="10" height="18"/></svg>
    <div><h3>Ecological Resilience</h3><p>To endure change Communities need to keep their watersheds functioning. Our network or professionals have decades of experience understanding and implementing conservation and restoration strategies.</p></div>
  </article>
  <article class="project-card">
    <svg class="project-icon" viewBox="0 0 64 64" fill="none" stroke="var(--green)" stroke-width="2"><circle cx="28" cy="30" r="22"/><path d="M10 24h36M10 36h30M28 8c-8 8-8 36 0 44"/><path d="M44 58c-8 0-12-6-10-12 2-5 6-6 6-12 6 4 12 10 12 16 0 5-3 8-8 8z" fill="#fff"/></svg>
    <div><h3>Energy and Food</h3><p>Security of community food and energy have, &amp; always will be, an essential component of how communities sustain themselves. Beyond the the ecological context managing a minimizing our resource demands will be essential.</p></div>
  </article>
</div>
<div class="abs projects-hub"></div>

<svg class="abs impact-bg" viewBox="0 0 1200 800" preserveAspectRatio="none">
  <defs><linearGradient id="impactFill" x1="0" y1="0" x2="0" y2="1"><stop offset="0" stop-color="#0b90d2"/><stop offset="1" stop-color="#0a7fc0"/></linearGradient></defs>
  <path d="M0 0H1200V780C1150 650 1060 560 900 530C760 505 620 520 480 520C260 520 80 460 0 330Z" fill="url(#impactFill)"/>
</svg>
<h2 class="abs serif impact-title">What We Are Doing ?<svg class="squiggle" viewBox="0 0 46 8"><path d="M1 4 Q6 0 11 4 T21 4 T31 4 T41 4" fill="none" stroke="#fff" stroke-width="2.5"/></svg></h2>

<div class="abs stat" style="left:107px">
  <svg viewBox="0 0 62 62" fill="none" stroke="#fff" stroke-width="2.5"><rect x="12" y="6" width="32" height="44" rx="3"/><path d="M19 16h18M19 24h18M19 32h12"/><circle cx="44" cy="46" r="9"/><path d="M40 46l3 3 5-6"/></svg>
  <div class="stat-num">15</div><div class="stat-label">Projects Completed</div>
</div>
<div class="abs stat" style="left:363px">
  <svg viewBox="0 0 62 62" fill="none" stroke="#fff" stroke-width="2.5"><circle cx="31" cy="24" r="16"/><path d="M36 18c-2-3-10-3-10 2s10 3 10 8-8 5-10 2M31 12v4M31 32v4"/><path d="M8 46l10-4h14c3 0 3 5 0 5H22M14 56h16l20-14"/></svg>
  <div class="stat-num">10</div><div class="stat-label">Donations</div>
</div>
<div class="abs stat" style="left:619px">
  <svg viewBox="0 0 62 62" fill="none" stroke="#fff" stroke-width="2.5"><circle cx="31" cy="20" r="9"/><circle cx="13" cy="24" r="6"/><circle cx="49" cy="24" r="6"/><path d="M16 52c0-10 6-18 15-18s15 8 15 18zM2 50c0-8 4-14 11-14M60 50c0-8-4-14-11-14"/></svg>
  <div class="stat-num">05</div><div class="stat-label">Communities</div>
</div>
<div class="abs stat" style="left:874px">
  <svg viewBox="0 0 62 62" fill="none" stroke="#fff" stroke-width="2.5"><path d="M31 42C18 32 12 26 12 18a9 9 0 0 1 19-3 9 9 0 0 1 19 3c0 8-6 14-19 24z"/><path d="M8 36l10 12h10M54 36L44 48H34"/></svg>
  <div class="stat-num">100</div><div class="stat-label">Volunteers</div>
</div>
<a class="abs btn btn-green impact-join">Join Us Today</a>
<a class="abs btn btn-white impact-contact">Contact Now</a>

<h2 class="abs serif section-title" style="top:2402px">Recent Work<svg class="squiggle" viewBox="0 0 46 8"><path d="M1 4 Q6 0 11 4 T21 4 T31 4 T41 4" fill="none" stroke="#ccc" stroke-width="2"/></svg></h2>
<div class="abs work-grid">
  <div class="work-tile" role="img" aria-label="A wind turbine above mountain ridges at dusk" style="background:linear-gradient(180deg,#8c8f94 0%,#b5a89a 45%,#6b5d4f 75%,#3f4a36 100%)"><h4>Energy</h4><span>Investing in clean energy</span></div>
  <div class="work-tile" role="img" aria-label="Terraced green fields with a small barn in golden light" style="background:linear-gradient(180deg,#6e6a5e 0%,#d8b574 35%,#8a7a3e 60%,#4c5d22 100%)"><h4>Food Security</h4><span>Retooling agriculture</span></div>
  <div class="work-tile" role="img" aria-label="Tidal flats in front of an industrial plant with smokestacks" style="background:linear-gradient(180deg,#c9d1d8 0%,#9aa6b0 40%,#4a5560 65%,#2a323a 100%)"><h4>Ecological Resilience</h4><span>Environmental Progress</span></div>
  <div class="work-tile" role="img" aria-label="A city road at night under a crescent moon" style="background:linear-gradient(180deg,#1f3a45 0%,#2e4a55 40%,#b06a4a 70%,#2a1c18 100%)"><h4>Infrastructure</h4><span>Lorem Ipsum</span></div>
</div>

<div class="abs green-frame"></div>
<div class="abs photo globe-photo" role="img" aria-label="A hand holding a glass sphere reflecting a forest"></div>
<h2 class="abs serif green-title">Think Green !<br>Save Money<svg class="squiggle" viewBox="0 0 46 8"><path d="M1 4 Q6 0 11 4 T21 4 T31 4 T41 4" fill="none" stroke="#ccc" stroke-width="2"/></svg></h2>
<div class="abs progress" style="top:3130px"><div class="label">Clean Water</div><div class="track"><div class="fill" style="width:355px;--c:var(--green)"></div></div><div class="pct">98%</div></div>
<div class="abs progress" style="top:3206px"><div class="label">Forest Rescue</div><div class="track"><div class="fill" style="width:203px;--c:var(--blue)"></div></div><div class="pct">56%</div></div>
<div class="abs progress" style="top:3283px"><div class="label">Agriculture</div><div class="track"><div class="fill" style="width:276px;--c:var(--blue)"></div></div><div class="pct">77%</div></div>
<div class="abs progress" style="top:3360px"><div class="label">Alternative Energy</div><div class="track"><div class="fill" style="width:330px;--c:var(--blue)"></div></div><div class="pct">84%</div></div>

<footer class="abs site-footer"></footer>
<div class="abs footer-brand">Corvane<br>Collective</div>
<h5 class="abs footer-head" style="left:388px;top:3636px">Contact Info</h5>
<div class="abs contact-item" style="top:3685px;color:#fff">
  <svg viewBox="0 0 14 14"><rect x="1" y="3" width="12" height="8" fill="var(--green)"/><path d="M1 3l6 5 6-5" stroke="#333" fill="none"/></svg>
  Email:<br>info@corvanecollective.org
</div>
<div class="abs contact-item" style="top:3746px">
  <svg viewBox="0 0 14 14"><path d="M3 1l3 3-2 2c1 2 2 3 4 4l2-2 3 3-2 2C6 13 1 8 1 3z" fill="var(--green)"/></svg>
  Phone:<br>360-555-0148
</div>
<div class="abs contact-item" style="top:3807px">
  <svg viewBox="0 0 14 14"><path d="M7 13C3 8 2 6 2 5a5 5 0 0 1 10 0c0 1-1 3-5 8z" fill="var(--green)"/><circle cx="7" cy="5" r="2" fill="#333"/></svg>
  Location:<br>2140 Alder Row, Mount<br>Hollis WA 98000
</div>
<h5 class="abs footer-head" style="left:654px;top:3636px">Qucik Links</h5>
<ul class="abs quick-links"><li>Home</li><li>About Us</li><li>Causes</li><li>Testimonial</li><li>Events</li><li>Contact Us</li></ul>
<h5 class="abs footer-head" style="left:853px;top:3638px">Newsletter</h5>
<p class="abs news-text">Subscribe to our email address to get the latest news.</p>
<div class="abs news-form">
  <svg class="abs" style="left:16px;top:15px" width="12" height="10" viewBox="0 0 12 10"><rect width="12" height="10" fill="#777"/><path d="M0 0l6 5 6-5" stroke="#fff" fill="none"/></svg>
  <span>Enter Your Email...</span>
  <div class="send"><svg width="16" height="16" viewBox="0 0 16 16"><path d="M1 8L15 1 11 15 8 9z" fill="#fff"/></svg></div>
</div>
<div class="abs social"><i style="background:#3b5998"></i><i style="background:#1da1f2"></i><i style="background:#d91c1c"></i><i style="background:#c13584"></i></div>
<div class="abs to-top"><svg width="14" height="16" viewBox="0 0 14 16"><path d="M7 15V2M2 7l5-5 5 5" stroke="#fff" stroke-width="1.6" fill="none"/></svg></div>
<p class="abs copyright">© Copyright 2020 &nbsp;&nbsp;|&nbsp;&nbsp; All Rights Reserved</p>

</body>
</html>
```